Business Card - Professional Minimalist - Double sided

We appreciate minimalist logo/web/collateral designs that allow design to tell a story. We want to relay a professional image/approach but throwing in a splash of modern when we’re able so long as it’s not distracting. Think 75% classic corporate, 25% modern. Open to black or white design, not sure which might look the best.

Target Market(s)

Senior executives or related government affairs contacts within the agriculture, energy, and defense industries (i.e., potential clients) but located outside of Washington, DC. Most potential clients based in DC with be familiar with both of us and our shared history.

Industry/Entity Type

Consulting

Contact Information for Business Card

Name: Daniel R. Whitlock
Title: Co-Founder & Partner
Address: 418 Bramblewood Ave. SE | Suite 2716 | Washington, D.C. 20019
Phone: (202) 555-0187
Email: Daniel@HollerbyWhitlock.com

Font styles to use
Serif

Colors

Designer to choose only greyscale colors for use in the design.

Requirements
Must have
• Name: Daniel R. Whitlock
Phone: (202) 555-0187

```html
<!DOCTYPE html>
<html lang="en">
<head>
<meta charset="utf-8">
<title>Hollerby Whitlock Group — Business Card</title>
<link rel="stylesheet" href="https://fonts.googleapis.com/css2?family=Alegreya+Sans:wght@400;700&display=swap">
<style>
  :root {
    --backdrop: #232224;
    --card: #151517;
    --brand-grey: #8a8a8e;
    --name-grey: #b9b9bd;
    --title-grey: #6f6f73;
    --detail-grey: #77777b;
    --card-shadow: rgba(0, 0, 0, 0.45);
  }
  * { box-sizing: border-box; margin: 0; padding: 0; }
  html, body {
    width: 1200px;
    height: 900px;
    overflow: hidden;
    background: var(--backdrop);
    font-family: "Alegreya Sans", sans-serif;
  }
  .sheet {
    width: 1200px;
    height: 900px;
    display: flex;
    flex-direction: column;
    align-items: center;
    justify-content: center;
    gap: 40px;
  }
  .card {
    position: relative;
    width: 700px;
    height: 400px;
    background: var(--card);
    box-shadow: 0 12px 30px var(--card-shadow);
  }
  .brand {
    position: absolute;
    display: flex;
    align-items: center;
    gap: 18px;
    color: var(--brand-grey);
    font-weight: 400;
  }
  .brand-square {
    width: 34px;
    height: 34px;
    background: var(--brand-grey);
    flex: none;
  }
  .brand-name {
    display: flex;
    flex-direction: column;
    align-items: flex-end;
    text-transform: uppercase;
    line-height: 1;
  }
  .brand-name .primary {
    font-size: 36px;
    letter-spacing: 0.04em;
  }
  .brand-name .secondary {
    font-size: 15px;
    letter-spacing: 0.55em;
    margin-top: 6px;
    margin-right: -0.55em;
  }
  .card-front .brand {
    left: 50%;
    top: 50%;
    transform: translate(-50%, -50%);
  }
  .card-back .brand {
    left: 105px;
    top: 70px;
  }
  .holder {
    position: absolute;
    left: 105px;
    bottom: 68px;
  }
  .holder-name {
    color: var(--name-grey);
    font-weight: 700;
    font-size: 28px;
    letter-spacing: 0.01em;
    text-transform: uppercase;
    line-height: 1.05;
  }
  .holder-title {
    color: var(--title-grey);
    font-size: 20px;
    line-height: 1.2;
  }
  .contact {
    position: absolute;
    left: 410px;
    top: 185px;
    color: var(--detail-grey);
    font-size: 18px;
    line-height: 1.25;
    font-style: normal;
  }
  .contact .gap { margin-top: 10px; }
</style>
</head>
<body>
  <main class="sheet">
    <section class="card card-front" aria-label="Card front">
      <div class="brand">
        <span class="brand-square" aria-hidden="true"></span>
        <div class="brand-name">
          <span class="primary">Hollerby Whitlock</span>
          <span class="secondary">Group</span>
        </div>
      </div>
    </section>

    <section class="card card-back" aria-label="Card back">
      <div class="brand">
        <span class="brand-square" aria-hidden="true"></span>
        <div class="brand-name">
          <span class="primary">Hollerby Whitlock</span>
          <span class="secondary">Group</span>
        </div>
      </div>

      <div class="holder">
        <p class="holder-name">Daniel R. Whitlock</p>
        <p class="holder-title">Co-Founder &amp; Partner</p>
      </div>

      <address class="contact">
        <p>418 Bramblewood Ave. SE</p>
        <p>Suite 2716</p>
        <p>Washington, D.C. 20019</p>
        <p class="gap">(202) 555-0187</p>
        <p>Daniel@HollerbyWhitlock.com</p>
      </address>
    </section>
  </main>
</body>
</html>
```